Bluewren Business Cards

Name Tomas Velikor
Title Mortgage Originator
Phone (800) 641-2705 x32
Direct (571) 362-8104
Email tvelikor@bluewrenhomeloans.example
NMLS #3804427
Name Lien Vo
Title Mortgage Originator
Location (800) 641-2705 x55
Direct (440) 296-5081
Email lvo@bluewrenhomeloans.example
NMLS #3719046
Name Solomon Ked-Ravi
Title Mortgage Originator
Location (800) 641-2705 x56
Direct (202) 374-6019
Email skedravi@bluewrenhomeloans.example
NMLS #3748510
Name Roselle Dunfield
Title Mortgage Originator
Location (800) 641-2705 x57
Direct (240) 538-2274
Email rdunfield@bluewrenhomeloans.example
NMLS #3692384
Name Dana Whitcombe
Title Mortgage Originator
Location (800) 641-2705 x58
Direct (540) 681-3926
Email dwhitcombe@bluewrenhomeloans.example
NMLS #3657019
Name Idris Holt
Title Mortgage Originator
Location (800) 641-2705 x59
Direct (240) 163-8852
Email iholt@bluewrenhomeloans.example
NMLS #3781462
Name Zora Lund
Title Mortgage Originator
Location (800) 641-2705 x60
Direct (202) 449-2637
Email zora@zorafindshomes.example
NMLS #3795038
Contact Information for Business Card
Name Tomas Velikor Title Mortgage Originator Phone (800) 641-2705 x32 Direct (571) 362-8104 Email tvelikor@bluewrenhomeloans.example NMLS #3804427 Name Lien Vo Title Mortgage Originator Location (800) 641-2705 x55 Direct (440) 296-5081 Email lvo@bluewrenhomeloans.example NMLS #3719046 Name Solomon Ked-Ravi Title Mortgage Originator Location (800) 641-2705 x56 Direct (202) 374-6019 Email skedravi@bluewrenhomeloans.example NMLS #3748510 Name Roselle Dunfield Title Mortgage Originator Location (800) 641-2705 x57 Direct (240) 538-2274 Email rdunfield@bluewrenhomeloans.example NMLS #3692384 Name Dana Whitcombe Title Mortgage Originator Location (800) 641-2705 x58 Direct (540) 681-3926 Email dwhitcombe@bluewrenhomeloans.example NMLS #3657019 Name Idris Holt Title Mortgage Originator Location (800) 641-2705 x59 Direct (240) 163-8852 Email iholt@bluewrenhomeloans.example NMLS #3781462 Name Zora Lund Title Mortgage Originator Location (800) 641-2705 x60 Direct (202) 449-2637 Email zora@zorafindshomes.example NMLS #3795038

```html
<!DOCTYPE html>
<html lang="en">
<head>
<meta charset="utf-8">
<title>Bluewren Business Cards</title>
<link rel="stylesheet" href="https://fonts.googleapis.com/css2?family=Crimson+Text:ital,wght@0,400;1,400&display=swap">
<style>
  :root {
    --backdrop: #7b5b3a;
    --card: #ffffff;
    --band: #111114;
    --ink: #1a1a1a;
    --navy: #1c3651;
    --mauve: #6b4a55;
  }
  * { margin: 0; padding: 0; box-sizing: border-box; }
  html, body { width: 1200px; height: 2315px; overflow: hidden; }
  body {
    background: var(--backdrop);
    position: relative;
    font-family: "Crimson Text", Georgia, serif;
    color: var(--ink);
  }
  .card {
    --accent: var(--ink);
    position: absolute;
    left: 189px;
    width: 836px;
    height: 477px;
    border-radius: 24px;
    overflow: hidden;
    background: var(--card);
    box-shadow: 0 4px 14px rgba(0,0,0,0.35);
  }
  .card--dana { top: 118px; }
  .card--lien { top: 652px; --accent: var(--navy); }
  .card--solomon { top: 1186px; --accent: var(--mauve); }
  .card--zora { top: 1721px; }
  .card-art { position: absolute; inset: 0; width: 836px; height: 477px; }
  .details {
    position: absolute;
    left: 430px;
    width: 392px;
    top: 0;
    height: 100%;
    text-align: center;
  }
  .details > * { position: absolute; left: 0; width: 100%; }
  .name {
    top: 48px;
    font-size: 33px;
    line-height: 1;
    text-transform: uppercase;
    letter-spacing: 0.3px;
    color: var(--accent);
    white-space: nowrap;
  }
  .role { top: 92px; font-size: 24px; line-height: 1; font-style: italic; }
  .icon { width: 28px; height: 28px; left: 182px; color: var(--accent); }
  .icon--office { top: 167px; }
  .icon--mobile { top: 246px; }
  .icon--email { top: 329px; }
  .line { font-size: 22px; line-height: 1; white-space: nowrap; }
  .line--office { top: 197px; }
  .line--mobile { top: 278px; }
  .line--email { top: 360px; font-size: 20px; }
  .line--nmls { top: 408px; }
  .rule {
    left: 50px;
    width: 292px;
    height: 1.5px;
    background: linear-gradient(90deg, transparent, var(--accent) 12%, var(--accent) 88%, transparent);
  }
  .rule--one { top: 235px; }
  .rule--two { top: 315px; }
</style>
</head>
<body>

<!-- Card: Dana Whitcombe -->
<section class="card card--dana">
  <svg class="card-art" viewBox="0 0 836 477">
    <defs>
      <linearGradient id="tone-dana" x1="0" y1="0" x2="1" y2="1">
        <stop offset="0" stop-color="#b49a86"/><stop offset="0.5" stop-color="#3a2a26"/><stop offset="1" stop-color="#1b1b1f"/>
      </linearGradient>
    </defs>
    <rect width="480" height="477" fill="url(#tone-dana)" role="img" aria-label="Portrait photo of Dana Whitcombe in a dark suit, holding a phone"/>
    <path d="M365,0 L480,0 L480,477 L343,477 Q446,238 365,0 Z" fill="var(--band)"/>
    <path d="M413,0 L836,0 L836,477 L343,477 Q482,238 413,0 Z" fill="var(--card)"/>
  </svg>
  <div class="details">
    <h2 class="name">Dana Whitcombe</h2>
    <p class="role">Mortgage Originator</p>
    <svg class="icon icon--office" viewBox="0 0 28 28"><circle cx="14" cy="14" r="12.5" fill="none" stroke="currentColor" stroke-width="1.8"/><path d="M10 8.5c1-.8 2-.6 2.4.3l.9 2c.2.6 0 1.1-.5 1.4l-.8.5c.5 1.5 1.7 3.2 3 4l.8-.6c.5-.3 1-.3 1.4.1l1.6 1.5c.6.6.5 1.5-.3 2.1-1.2 1-3 .9-4.8-.6-2.3-2-4-4.8-4.4-7.1-.2-1.4.2-2.8.7-3.6z" fill="currentColor"/></svg>
    <p class="line line--office">(800) 641-2705 x58</p>
    <div class="rule rule--one"></div>
    <svg class="icon icon--mobile" viewBox="0 0 28 28"><circle cx="14" cy="14" r="12.5" fill="none" stroke="currentColor" stroke-width="1.8"/><rect x="9.5" y="7.5" width="9" height="13" rx="1.6" fill="none" stroke="currentColor" stroke-width="1.8"/><rect x="11.3" y="9.5" width="5.4" height="8" fill="currentColor" opacity="0.25"/></svg>
    <p class="line line--mobile">(540) 681-3926</p>
    <div class="rule rule--two"></div>
    <svg class="icon icon--email" viewBox="0 0 28 28"><circle cx="14" cy="14" r="12.5" fill="currentColor"/><rect x="7.5" y="9.5" width="13" height="9" fill="#fff"/><path d="M7.5 9.5 L14 14.5 L20.5 9.5 M7.5 18.5 L12 13.5 M20.5 18.5 L16 13.5" fill="none" stroke="currentColor" stroke-width="1.2"/></svg>
    <p class="line line--email">dwhitcombe@bluewrenhomeloans.example</p>
    <p class="line line--nmls">NMLS #3657019</p>
  </div>
</section>

<!-- Card: Lien Vo -->
<section class="card card--lien">
  <svg class="card-art" viewBox="0 0 836 477">
    <defs>
      <linearGradient id="tone-lien" x1="0" y1="0" x2="0" y2="1">
        <stop offset="0" stop-color="#b8aca0"/><stop offset="0.6" stop-color="#8a7d72"/><stop offset="1" stop-color="#1f3650"/>
      </linearGradient>
    </defs>
    <rect width="480" height="477" fill="url(#tone-lien)" role="img" aria-label="Portrait photo of Lien Vo in a navy suit and glasses"/>
    <path d="M365,0 L480,0 L480,477 L343,477 Q446,238 365,0 Z" fill="var(--band)"/>
    <path d="M413,0 L836,0 L836,477 L343,477 Q482,238 413,0 Z" fill="var(--card)"/>
  </svg>
  <div class="details">
    <h2 class="name">Lien Vo</h2>
    <p class="role">Mortgage Originator</p>
    <svg class="icon icon--office" viewBox="0 0 28 28"><circle cx="14" cy="14" r="12.5" fill="none" stroke="currentColor" stroke-width="1.8"/><path d="M10 8.5c1-.8 2-.6 2.4.3l.9 2c.2.6 0 1.1-.5 1.4l-.8.5c.5 1.5 1.7 3.2 3 4l.8-.6c.5-.3 1-.3 1.4.1l1.6 1.5c.6.6.5 1.5-.3 2.1-1.2 1-3 .9-4.8-.6-2.3-2-4-4.8-4.4-7.1-.2-1.4.2-2.8.7-3.6z" fill="currentColor"/></svg>
    <p class="line line--office">(800) 641-2705 x55</p>
    <div class="rule rule--one"></div>
    <svg class="icon icon--mobile" viewBox="0 0 28 28"><circle cx="14" cy="14" r="12.5" fill="none" stroke="currentColor" stroke-width="1.8"/><rect x="9.5" y="7.5" width="9" height="13" rx="1.6" fill="none" stroke="currentColor" stroke-width="1.8"/><rect x="11.3" y="9.5" width="5.4" height="8" fill="currentColor" opacity="0.25"/></svg>
    <p class="line line--mobile">(440) 296-5081</p>
    <div class="rule rule--two"></div>
    <svg class="icon icon--email" viewBox="0 0 28 28"><circle cx="14" cy="14" r="12.5" fill="currentColor"/><rect x="7.5" y="9.5" width="13" height="9" fill="#fff"/><path d="M7.5 9.5 L14 14.5 L20.5 9.5 M7.5 18.5 L12 13.5 M20.5 18.5 L16 13.5" fill="none" stroke="currentColor" stroke-width="1.2"/></svg>
    <p class="line line--email">lvo@bluewrenhomeloans.example</p>
    <p class="line line--nmls">NMLS #3719046</p>
  </div>
</section>

<!-- Card: Solomon Ked-Ravi -->
<section class="card card--solomon">
  <svg class="card-art" viewBox="0 0 836 477">
    <defs>
      <linearGradient id="tone-solomon" x1="0" y1="0" x2="0" y2="1">
        <stop offset="0" stop-color="#2e4260"/><stop offset="0.55" stop-color="#3a3a48"/><stop offset="1" stop-color="#5e3e44"/>
      </linearGradient>
    </defs>
    <rect width="480" height="477" fill="url(#tone-solomon)" role="img" aria-label="Portrait photo of Solomon Ked-Ravi in a burgundy blazer and black turtleneck"/>
    <path d="M365,0 L480,0 L480,477 L343,477 Q446,238 365,0 Z" fill="var(--band)"/>
    <path d="M413,0 L836,0 L836,477 L343,477 Q482,238 413,0 Z" fill="var(--card)"/>
  </svg>
  <div class="details">
    <h2 class="name">Solomon Ked-Ravi</h2>
    <p class="role">Mortgage Originator</p>
    <svg class="icon icon--office" viewBox="0 0 28 28"><circle cx="14" cy="14" r="12.5" fill="none" stroke="currentColor" stroke-width="1.8"/><path d="M10 8.5c1-.8 2-.6 2.4.3l.9 2c.2.6 0 1.1-.5 1.4l-.8.5c.5 1.5 1.7 3.2 3 4l.8-.6c.5-.3 1-.3 1.4.1l1.6 1.5c.6.6.5 1.5-.3 2.1-1.2 1-3 .9-4.8-.6-2.3-2-4-4.8-4.4-7.1-.2-1.4.2-2.8.7-3.6z" fill="currentColor"/></svg>
    <p class="line line--office">(800) 641-2705 x56</p>
    <div class="rule rule--one"></div>
    <svg class="icon icon--mobile" viewBox="0 0 28 28"><circle cx="14" cy="14" r="12.5" fill="none" stroke="currentColor" stroke-width="1.8"/><rect x="9.5" y="7.5" width="9" height="13" rx="1.6" fill="none" stroke="currentColor" stroke-width="1.8"/><rect x="11.3" y="9.5" width="5.4" height="8" fill="currentColor" opacity="0.25"/></svg>
    <p class="line line--mobile">(202) 374-6019</p>
    <div class="rule rule--two"></div>
    <svg class="icon icon--email" viewBox="0 0 28 28"><circle cx="14" cy="14" r="12.5" fill="currentColor"/><rect x="7.5" y="9.5" width="13" height="9" fill="#fff"/><path d="M7.5 9.5 L14 14.5 L20.5 9.5 M7.5 18.5 L12 13.5 M20.5 18.5 L16 13.5" fill="none" stroke="currentColor" stroke-width="1.2"/></svg>
    <p class="line line--email">skedravi@bluewrenhomeloans.example</p>
    <p class="line line--nmls">NMLS #3748510</p>
  </div>
</section>

<!-- Card: Zora Lund -->
<section class="card card--zora">
  <svg class="card-art" viewBox="0 0 836 477">
    <defs>
      <linearGradient id="tone-zora" x1="0" y1="0" x2="0" y2="1">
        <stop offset="0" stop-color="#d8d4d2"/><stop offset="0.5" stop-color="#c9c3c0"/><stop offset="1" stop-color="#eeeae6"/>
      </linearGradient>
    </defs>
    <rect width="480" height="477" fill="url(#tone-zora)" role="img" aria-label="Portrait photo of Zora Lund in a white blazer"/>
    <path d="M365,0 L480,0 L480,477 L343,477 Q446,238 365,0 Z" fill="var(--band)"/>
    <path d="M413,0 L836,0 L836,477 L343,477 Q482,238 413,0 Z" fill="var(--card)"/>
  </svg>
  <div class="details">
    <h2 class="name">Zora Lund</h2>
    <p class="role">Mortgage Originator</p>
    <svg class="icon icon--office" viewBox="0 0 28 28"><circle cx="14" cy="14" r="12.5" fill="none" stroke="currentColor" stroke-width="1.8"/><path d="M10 8.5c1-.8 2-.6 2.4.3l.9 2c.2.6 0 1.1-.5 1.4l-.8.5c.5 1.5 1.7 3.2 3 4l.8-.6c.5-.3 1-.3 1.4.1l1.6 1.5c.6.6.5 1.5-.3 2.1-1.2 1-3 .9-4.8-.6-2.3-2-4-4.8-4.4-7.1-.2-1.4.2-2.8.7-3.6z" fill="currentColor"/></svg>
    <p class="line line--office">(800) 641-2705 x60</p>
    <div class="rule rule--one"></div>
    <svg class="icon icon--mobile" viewBox="0 0 28 28"><circle cx="14" cy="14" r="12.5" fill="none" stroke="currentColor" stroke-width="1.8"/><rect x="9.5" y="7.5" width="9" height="13" rx="1.6" fill="none" stroke="currentColor" stroke-width="1.8"/><rect x="11.3" y="9.5" width="5.4" height="8" fill="currentColor" opacity="0.25"/></svg>
    <p class="line line--mobile">(202) 449-2637</p>
    <div class="rule rule--two"></div>
    <svg class="icon icon--email" viewBox="0 0 28 28"><circle cx="14" cy="14" r="12.5" fill="currentColor"/><rect x="7.5" y="9.5" width="13" height="9" fill="#fff"/><path d="M7.5 9.5 L14 14.5 L20.5 9.5 M7.5 18.5 L12 13.5 M20.5 18.5 L16 13.5" fill="none" stroke="currentColor" stroke-width="1.2"/></svg>
    <p class="line line--email">zora@zorafindshomes.example</p>
    <p class="line line--nmls">NMLS #3795038</p>
  </div>
</section>

</body>
</html>
```